Please look at my website to get a better understanding of my business: www.perovatu.com
This business is about Life Coaching for Families, couples, teenagers and individuals. I work more w parents of teenagers (as well as teenagers) but not so much with young kids.
The card should be fun, not too busy, with a sense of flow and playfulness. Warm colors, artistic style (can have a family sculpture, paining or a picture in it). Basic information about myself and my company

Reason: I extended my due date for next Tuesday, November 13th. Please summit new designs if you haven't done so, and for those who submitted, thank you so much for your time and effort. I will make a decision next Tues, and will contact you if I need to revise some items. Much thanks to you all! Orla

Families, parents, teenagers, couples, individuals.

Business

• Business name: PeRoVaTu! Hearth Circle Life Coaching
My name: Orla Bekwith, RMTQ
Description of my work: Tri-Mode life coach
Tel: 555-304-7719
Website: www.PeRoVaTu.com
• Family sculpture, abstract painting or a picture, or simply a nice background w/out a picture added.
• Corporate feeling, cold colors, corporate symbols. no Sunset, or picture of families on the beach.
Don't include bar-code (from uploaded file 1, it is only the designer to find out more about my website).

```html
<!DOCTYPE html>
<html lang="en">
<head>
<meta charset="utf-8">
<title>PeRoVaTu Business Cards</title>
<link rel="stylesheet" href="https://fonts.googleapis.com/css2?family=Arimo:wght@400;700&display=swap">
<style>
  :root {
    --page: #ffffff;
    --gold: #b3893d;
    --gold-light: #c49a4c;
    --orange: #c0601c;
    --orange-glow: #d97a22;
    --rust: #a23a14;
    --rust-deep: #8f2a10;
    --ink-light: #ffffff;
    --shadow: rgba(0, 0, 0, 0.45);
  }
  * { margin: 0; padding: 0; box-sizing: border-box; }
  html, body {
    width: 1200px;
    height: 1000px;
    overflow: hidden;
    background: var(--page);
    font-family: "Arimo", Arial, sans-serif;
    color: var(--ink-light);
  }
  .canvas {
    position: relative;
    width: 1200px;
    height: 1000px;
  }
  .card {
    position: absolute;
    top: 187px;
    width: 348px;
    height: 627px;
    overflow: hidden;
    box-shadow: 9px 9px 9px var(--shadow);
  }
  .card--front { left: 55px; }
  .card--back-a { left: 424px; }
  .card--back-b { left: 796px; }
  .card__bg {
    position: absolute;
    inset: 0;
    width: 100%;
    height: 100%;
  }
  .card__content { position: absolute; inset: 0; }

  .tagline {
    position: absolute;
    left: 295px;
    top: 460px;
    transform: rotate(-90deg);
    transform-origin: 0 0;
    font-weight: 700;
    font-size: 26px;
    letter-spacing: 0.5px;
    white-space: nowrap;
  }
  .wordmark {
    position: absolute;
    left: 22px;
    top: 515px;
    font-weight: 700;
    font-size: 52px;
    letter-spacing: 1px;
    white-space: nowrap;
  }

  .service-title {
    position: absolute;
    left: 40px;
    top: 16px;
    font-size: 38px;
    line-height: 42px;
    font-weight: 400;
  }
  .contact {
    position: absolute;
    left: 16px;
    right: 14px;
    top: 472px;
    text-align: right;
    white-space: nowrap;
  }
  .contact__name { font-size: 30px; line-height: 34px; word-spacing: 3px; }
  .contact__role { font-size: 20px; line-height: 22px; word-spacing: 2px; }
  .contact__tel { font-size: 27px; line-height: 30px; margin-top: 16px; word-spacing: 3px; }
  .contact__web { font-size: 21px; line-height: 26px; margin-top: 4px; word-spacing: 2px; }
</style>
</head>
<body>
<main class="canvas">

  <section class="card card--front">
    <svg class="card__bg" viewBox="0 0 260 470" preserveAspectRatio="none" aria-hidden="true">
      <defs>
        <radialGradient id="glow-front" cx="0.5" cy="0.5" r="0.6">
          <stop offset="0" stop-color="var(--orange-glow)"/>
          <stop offset="1" stop-color="var(--orange)"/>
        </radialGradient>
        <linearGradient id="gold-front" x1="0" y1="0" x2="0" y2="1">
          <stop offset="0" stop-color="var(--gold)"/>
          <stop offset="1" stop-color="var(--gold-light)"/>
        </linearGradient>
      </defs>
      <rect width="260" height="470" fill="url(#glow-front)"/>
      <path d="M0 0 H260 V125 C190 110 120 140 60 130 C35 126 15 120 0 118 Z" fill="url(#gold-front)"/>
      <path d="M0 250 C70 280 150 300 260 345 V470 H0 Z" fill="var(--rust)"/>
    </svg>
    <div class="card__content">
      <p class="tagline">HARMONY IN YOUR HOME</p>
      <p class="wordmark">PeRoVaTu</p>
    </div>
  </section>

  <section class="card card--back-a">
    <svg class="card__bg" viewBox="0 0 260 470" preserveAspectRatio="none" aria-hidden="true">
      <defs>
        <radialGradient id="glow-a" cx="0.45" cy="0.55" r="0.6">
          <stop offset="0" stop-color="var(--orange-glow)"/>
          <stop offset="1" stop-color="var(--orange)"/>
        </radialGradient>
      </defs>
      <rect width="260" height="470" fill="url(#glow-a)"/>
      <path d="M0 0 H260 V132 C200 115 140 160 70 148 C40 143 20 140 0 142 Z" fill="var(--gold)"/>
      <path d="M0 325 C80 345 170 370 260 360 V470 H0 Z" fill="var(--rust-deep)"/>
    </svg>
    <div class="card__content">
      <h2 class="service-title">Hearth<br>Circle<br>Life<br>Coaching</h2>
      <div class="contact">
        <p class="contact__name">Orla Bekwith, RMTQ</p>
        <p class="contact__role">Tri-Mode life coach</p>
        <p class="contact__tel">Tel: 555-304-7719</p>
        <p class="contact__web">Website: www.PeRoVaTu.com</p>
      </div>
    </div>
  </section>

  <section class="card card--back-b">
    <svg class="card__bg" viewBox="0 0 260 470" preserveAspectRatio="none" aria-hidden="true">
      <defs>
        <radialGradient id="glow-b" cx="0.45" cy="0.55" r="0.6">
          <stop offset="0" stop-color="var(--orange-glow)"/>
          <stop offset="1" stop-color="var(--orange)"/>
        </radialGradient>
      </defs>
      <rect width="260" height="470" fill="url(#glow-b)"/>
      <path d="M0 0 H260 V132 C200 115 140 160 70 148 C40 143 20 140 0 142 Z" fill="var(--gold)"/>
      <path d="M0 325 C80 345 170 370 260 360 V470 H0 Z" fill="var(--rust-deep)"/>
    </svg>
    <div class="card__content">
      <h2 class="service-title">Hearth<br>Circle<br>Life<br>Coaching</h2>
      <div class="contact">
        <p class="contact__name">Orla Bekwith, RMTQ</p>
        <p class="contact__role">Tri-Mode life coach</p>
        <p class="contact__tel">Tel: 555-304-7719</p>
        <p class="contact__web">Website: www.PeRoVaTu.com</p>
      </div>
    </div>
  </section>

</main>
</body>
</html>
```